3 out of 100 people will get deadly skin cancer - we need a great illustration that shows this!

We put together a prototype image that communicates lifetime skin cancer risk. (see attached). We are looking for illustrators who can take make a new/better/cooler graphic that communicates this idea. It could be as simple as a superior illustration of the graphic we have or illustrators can propose a completely different idea.What should the illustration communicate?U.S. adults have a lifetime risk of developing skin cancer of 1 in 5. But we don't want to show 1 in 5; we want to show that number in a larger group. For example, in the attached illustration we show 20 in 100 people get skin cancer (i.e., 100 beach towels/umbrellas and 20 of them are red). Research has shown that people are more likely to accurately understand numbers like this when you convey them for larger groups (i.e., 20 out of 100 rather than 1 out of 5). U.S. adults also have a lifetime risk of 2.3% of developing the deadliest form of skin cancer (melanoma). In other words, approximately 3 in 100 people will develop melanoma in their lifetime. Ideally, a single image will convey both lifetime skin cancer risk (20 in 100) and melanoma risk (3 in 100). We will award a top three as follows: 1st place = $300, 2nd place = $250, third place = $200. We will also buy any design beyond 3rd place that we like for $100. For example, we purchased 24 designs in our last contest on Artmarketly.This research is supported by funding from the Corvane Institute of Science.

Target Market(s)

The U.S. public; individuals at high risk of developing skin cancer

Industry/Entity Type

Medicine

Colors

Designer to choose colors to be used in the design.

Requirements
Must have
• an original illustration that conveys both lifetime risk of developing skin cancer (20 in 100) and melanoma (3 in 100).
Nice to have
• It can be beach towels and umbrellas, just like our prototype, or the designers can pitch an original idea. Imagery can be realistic or cartoonish (or something in between). It should be illustrations, though. Not edited photos. The image should be in color (no black and white illustrations).
Should not have
• Photos. Clip art. Free vector images.
• We are looking for original illustrations created by the designer.

```html
<!DOCTYPE html>
<html lang="en">
<head>
<meta charset="utf-8">
<title>Lifetime Skin Cancer Risk</title>
<link href="https://fonts.googleapis.com/css2?family=Arimo:wght@700&display=swap" rel="stylesheet">
<style>
  :root {
    --bg-center: #fdeadb;
    --bg-edge: #f8d1a6;
    --no-cancer: #8a4a9c;
    --skin-cancer: #d2762c;
    --melanoma: #e8242e;
    --hair: #6b3a22;
    --ink: #8b5a2e;
    --frame: #9a6a44;
  }
  html, body {
    margin: 0;
    padding: 0;
    overflow: hidden;
  }
  .poster {
    position: relative;
    width: 933px;
    height: 1200px;
    overflow: hidden;
    background: radial-gradient(ellipse at 50% 50%, var(--bg-center) 0%, var(--bg-edge) 100%);
    font-family: "Arimo", Arial, sans-serif;
    font-weight: 700;
    color: var(--ink);
  }

  /* 100-unit risk grid: each unit stands for one adult */
  .group {
    position: absolute;
    width: 304px;
    height: 112px;
    display: flex;
    justify-content: space-between;
  }
  .group.left { left: 136px; }
  .group.right { left: 503px; }
  .row-1 { top: 67px; }
  .row-2 { top: 204px; }
  .row-3 { top: 340px; }
  .row-4 { top: 478px; }
  .row-5 { top: 633px; }

  .unit {
    --body: var(--no-cancer);
    width: 25px;
    height: 100%;
    border-radius: 13px 13px 3px 3px;
    background: linear-gradient(180deg, var(--hair) 0 17%, var(--body) 17% 100%);
  }
  .unit.skin { --body: var(--skin-cancer); }
  .unit.melanoma {
    --body: var(--melanoma);
    box-shadow: inset 0 0 0 2px var(--melanoma);
  }

  .fact-box {
    position: absolute;
    left: 29px;
    top: 771px;
    width: 877px;
    height: 207px;
    box-sizing: border-box;
    border: 1px solid var(--frame);
    text-align: center;
    font-size: 26px;
    line-height: 31px;
    padding-top: 19px;
  }
  .fact-box p { margin: 0; }
  .fact-box .gap { margin-top: 5px; }

  .legend-item {
    position: absolute;
    top: 1035px;
    height: 111px;
  }
  .legend-item .unit {
    position: absolute;
    left: 0;
    top: 0;
    width: 52px;
    height: 111px;
    border-radius: 26px 26px 3px 3px;
  }
  .legend-label {
    position: absolute;
    bottom: -3px;
    white-space: nowrap;
    font-size: 26px;
    line-height: 1;
  }
  .legend-no-cancer { left: 72px; }
  .legend-no-cancer .legend-label { left: 51px; }
  .legend-skin-cancer { left: 372px; }
  .legend-skin-cancer .legend-label { left: 50px; }
  .legend-melanoma { left: 696px; }
  .legend-melanoma .legend-label { left: 52px; }
</style>
</head>
<body>
<main class="poster">
  <section class="risk-grid" aria-label="100 adults: 17 with skin cancer and 3 with melanoma">
    <div class="group left row-1">
      <span class="unit"></span><span class="unit"></span><span class="unit skin"></span><span class="unit"></span><span class="unit"></span>
      <span class="unit skin"></span><span class="unit"></span><span class="unit"></span><span class="unit"></span><span class="unit"></span>
    </div>
    <div class="group right row-1">
      <span class="unit"></span><span class="unit"></span><span class="unit"></span><span class="unit"></span><span class="unit skin"></span>
      <span class="unit"></span><span class="unit"></span><span class="unit"></span><span class="unit skin"></span><span class="unit"></span>
    </div>
    <div class="group left row-2">
      <span class="unit"></span><span class="unit skin"></span><span class="unit"></span><span class="unit"></span><span class="unit"></span>
      <span class="unit"></span><span class="unit"></span><span class="unit"></span><span class="unit skin"></span><span class="unit"></span>
    </div>
    <div class="group right row-2">
      <span class="unit"></span><span class="unit"></span><span class="unit"></span><span class="unit melanoma"></span><span class="unit"></span>
      <span class="unit"></span><span class="unit"></span><span class="unit"></span><span class="unit"></span><span class="unit"></span>
    </div>
    <div class="group left row-3">
      <span class="unit"></span><span class="unit"></span><span class="unit"></span><span class="unit skin"></span><span class="unit"></span>
      <span class="unit"></span><span class="unit"></span><span class="unit skin"></span><span class="unit"></span><span class="unit"></span>
    </div>
    <div class="group right row-3">
      <span class="unit skin"></span><span class="unit"></span><span class="unit skin"></span><span class="unit"></span><span class="unit"></span>
      <span class="unit"></span><span class="unit"></span><span class="unit"></span><span class="unit"></span><span class="unit"></span>
    </div>
    <div class="group left row-4">
      <span class="unit"></span><span class="unit"></span><span class="unit"></span><span class="unit skin"></span><span class="unit"></span>
      <span class="unit"></span><span class="unit"></span><span class="unit skin"></span><span class="unit"></span><span class="unit"></span>
    </div>
    <div class="group right row-4">
      <span class="unit"></span><span class="unit melanoma"></span><span class="unit"></span><span class="unit"></span><span class="unit"></span>
      <span class="unit"></span><span class="unit"></span><span class="unit skin"></span><span class="unit"></span><span class="unit"></span>
    </div>
    <div class="group left row-5">
      <span class="unit"></span><span class="unit skin"></span><span class="unit"></span><span class="unit skin"></span><span class="unit"></span>
      <span class="unit"></span><span class="unit"></span><span class="unit"></span><span class="unit"></span><span class="unit melanoma"></span>
    </div>
    <div class="group right row-5">
      <span class="unit skin"></span><span class="unit"></span><span class="unit"></span><span class="unit"></span><span class="unit"></span>
      <span class="unit skin"></span><span class="unit"></span><span class="unit"></span><span class="unit"></span><span class="unit"></span>
    </div>
  </section>

  <section class="fact-box">
    <p>Research says 20 out of 100 adults in U.S have lifetime risk</p>
    <p>of developing a skin cancer</p>
    <p class="gap">out of which 2.3% have lifetime risk of developing a melanoma,</p>
    <p>the deadliest form of skin cancer.</p>
    <p>So, the probability of melanoma is 3 out of 100</p>
  </section>

  <section class="legend">
    <div class="legend-item legend-no-cancer">
      <span class="unit"></span>
      <span class="legend-label">No Cancer</span>
    </div>
    <div class="legend-item legend-skin-cancer">
      <span class="unit skin"></span>
      <span class="legend-label">Skin Cancer</span>
    </div>
    <div class="legend-item legend-melanoma">
      <span class="unit melanoma"></span>
      <span class="legend-label">Melanoma</span>
    </div>
  </section>
</main>
</body>
</html>
```